Ice cream manufacturer need packaging design

We are a artisanal ice cream maker - Gelato makers - we are in the process of commercialising our products to restaurants, hotels. catering services and large supermarkets. It is a unique product which we are bringing to the market as it is a traditionally made ice cream using fresh ingredients rather than flavouring. We will be selling our products in small individual containers of 100ml as well as family boxes of 500ml and 1l. A little bit like Brellovin.We need the packaging to ooze quality, it needs to scream that' this is not your average industrial air full ice cream, but quality natural ingredients'The packaging needs to include:- The brand name Plenta as a nice logo- The flavour- Ingredients section.- Batch number- Expire date (should read see lid)- The name and address of the manufacturer - Sweet Harbor, Rue Kamel Ferhani, Draria, Alger, Algerie - Special storage conditions - To be stored at -18 degrees and left at room temperature for 10 min before consumption.- Net weight: 100ml or 500ml or 1l

Industry/Entity Type

Food Production

Colors

Designer to choose colors to be used in the design.

Requirements
Must have
• Brand Name and Flavour with some reference to ice cream.
Nice to have
• It must convey that this is a quality product.
Should not have
• It should not have a funny or playful message

```html
<!DOCTYPE html>
<html lang="en">
<head>
<meta charset="utf-8">
<title>Plenta Gelato – Vanilla 100ml Packaging</title>
<link rel="stylesheet" href="https://fonts.googleapis.com/css2?family=Arimo:ital,wght@0,400;0,700;1,400&family=Parisienne&display=swap">
<style>
  :root {
    --canvas-bg: #ffffff;
    --brand-red: #e3140f;
    --ring-red-light: #f4441c;
    --ring-red-dark: #a31404;
    --ring-orange-light: #ffc24a;
    --ring-orange-dark: #e8860a;
    --cream-light: #fbf3e6;
    --cream-mid: #efdcc0;
    --cream-warm: #e6c39a;
    --mist-light: #f1f2f3;
    --mist-mid: #c9cbcd;
    --label-white: #ffffff;
    --flavour-brown: #6b4c1c;
    --text-dark: #2a2a2a;
    --text-mid: #444444;
  }
  * { margin: 0; padding: 0; box-sizing: border-box; }
  html, body {
    width: 1200px;
    height: 857px;
    overflow: hidden;
    background: var(--canvas-bg);
  }
  .canvas {
    position: relative;
    width: 1200px;
    height: 857px;
    background: var(--canvas-bg);
  }
  .lid-label {
    position: absolute;
    left: 82px;
    top: 169px;
    width: 424px;
    height: 424px;
  }
  .tub-label {
    position: absolute;
    left: 545px;
    top: 255px;
    width: 470px;
    height: 500px;
  }
  .brand-name {
    font-family: "Arimo", Arial, sans-serif;
    font-weight: 700;
    fill: var(--brand-red);
  }
  .product-type {
    font-family: "Arimo", Arial, sans-serif;
    font-weight: 400;
    fill: var(--text-mid);
  }
  .flavour-name {
    font-family: "Parisienne", cursive;
    fill: var(--flavour-brown);
  }
  .net-volume {
    font-family: "Arimo", Arial, sans-serif;
    font-weight: 700;
    fill: var(--text-dark);
  }
  .lid-volume {
    font-family: "Arimo", Arial, sans-serif;
    fill: var(--text-dark);
  }
  .batch-line {
    font-family: "Arimo", Arial, sans-serif;
    font-style: italic;
    fill: var(--text-mid);
  }
  .maker-name {
    font-family: "Arimo", Arial, sans-serif;
    font-weight: 700;
    fill: var(--text-dark);
  }
  .maker-address {
    font-family: "Arimo", Arial, sans-serif;
    fill: var(--text-dark);
  }
</style>
</head>
<body>
<main class="canvas">

  <!-- Lid label -->
  <svg class="lid-label" viewBox="0 0 424 424" xmlns="http://www.w3.org/2000/svg">
    <defs>
      <radialGradient id="lid-orange-ring" cx="50%" cy="45%" r="55%">
        <stop offset="80%" stop-color="var(--ring-orange-dark)"/>
        <stop offset="100%" stop-color="var(--ring-orange-light)"/>
      </radialGradient>
      <linearGradient id="lid-red-ring" x1="0" y1="0" x2="1" y2="1">
        <stop offset="0%" stop-color="var(--ring-red-light)"/>
        <stop offset="100%" stop-color="var(--ring-red-dark)"/>
      </linearGradient>
      <radialGradient id="lid-gelato" cx="50%" cy="40%" r="60%">
        <stop offset="0%" stop-color="var(--cream-light)"/>
        <stop offset="70%" stop-color="var(--cream-mid)"/>
        <stop offset="100%" stop-color="var(--cream-warm)"/>
      </radialGradient>
    </defs>
    <circle cx="212" cy="212" r="210" fill="url(#lid-orange-ring)"/>
    <circle cx="212" cy="212" r="178" fill="url(#lid-red-ring)"/>
    <circle cx="212" cy="212" r="143" fill="url(#lid-gelato)" role="img" aria-label="Photograph of scooped vanilla gelato with toasted marshmallow pieces"/>
    <text class="brand-name" x="212" y="190" font-size="54" text-anchor="middle">Plenta</text>
    <text class="product-type" x="212" y="209" font-size="11" text-anchor="middle">Gelato Ice cream</text>
    <text class="flavour-name" x="212" y="265" font-size="38" text-anchor="middle">Vanilla</text>
    <text class="lid-volume" x="212" y="324" font-size="14" text-anchor="middle">100ml</text>
  </svg>

  <!-- Tub wrap label -->
  <svg class="tub-label" viewBox="0 0 470 500" xmlns="http://www.w3.org/2000/svg">
    <defs>
      <linearGradient id="tub-mist" x1="0" y1="0" x2="1" y2="0">
        <stop offset="0%" stop-color="var(--mist-mid)"/>
        <stop offset="50%" stop-color="var(--mist-light)"/>
        <stop offset="100%" stop-color="var(--mist-mid)"/>
      </linearGradient>
      <radialGradient id="tub-gelato" cx="50%" cy="40%" r="60%">
        <stop offset="0%" stop-color="var(--cream-light)"/>
        <stop offset="70%" stop-color="var(--cream-mid)"/>
        <stop offset="100%" stop-color="var(--cream-warm)"/>
      </radialGradient>
    </defs>
    <rect x="0" y="0" width="470" height="500" fill="var(--label-white)"/>
    <rect x="6" y="15" width="458" height="425" rx="18" fill="url(#tub-mist)" role="img" aria-label="Frosted background with condensation droplets and dripping edges"/>
    <circle cx="239" cy="200" r="182" fill="url(#tub-gelato)" role="img" aria-label="Photograph of scooped vanilla gelato with toasted marshmallow pieces"/>
    <text class="brand-name" x="239" y="178" font-size="80" text-anchor="middle">Plenta</text>
    <text class="product-type" x="239" y="205" font-size="19" text-anchor="middle">Gelato Ice cream</text>
    <text class="flavour-name" x="239" y="303" font-size="50" text-anchor="middle">Vanilla</text>
    <text class="net-volume" x="235" y="418" font-size="15" text-anchor="middle">100ml</text>
    <text class="batch-line" x="235" y="435" font-size="11" text-anchor="middle">N0.32454567. Exp.Oct2019</text>
    <text class="maker-name" x="235" y="463" font-size="13" text-anchor="middle">Sweet Harbor,</text>
    <text class="maker-address" x="235" y="480" font-size="13" text-anchor="middle">Rue Kamel Ferhani,Draria Algier, Algeria</text>
  </svg>

</main>
</body>
</html>
```